Consulting/ Manufacturers Representative Website

I need a website for a consulting/manufacturer representative company in Texas called Birchwell Venture Advisors. We Uncover and implement the right solution, at the right time, in the right way. We consult, we train, we offer project management, we offer performance improvement, we offer value creation, we turn stagnation into growth, and we offer corporate performance improvement.
I want the design to load on desktop and mobile, I want the site to look and feel professional like a large firm, and I want the site to be a marketing tool and establish a strong online presence.

Target Market(s)

City Governments, State Governments, County Governments, US Government, Power Plants, Refineries, Chemical Plants, Industrial customers

Industry/Entity Type

Consulting

Number of Pages Required

5+ page

Requirements
Must have
• mobile and desktop compatible, professional look, must be a fast website, company email and contact capabilities, contact page, company logo on website, SEO optimized, must display different industries served: Energy, Public (Government, Not For Profit, Educational), Transportation & Logistics, Business Services.
• Show that I help customers operate in a cleaner, safer and more economical way.
Nice to have
• news letter, news feed, show that company is principles based.
Should not have
• slow site, cheap look

```html
<!DOCTYPE html>
<html lang="en">
<head>
<meta charset="utf-8">
<title>Birchwell Venture Advisors</title>
<link href="https://fonts.googleapis.com/css2?family=Open+Sans:wght@400;600;700&family=Oswald:wght@400;500&display=swap" rel="stylesheet">
<style>
:root{
  --blue:#3592dd;
  --blue-dark:#2a7cc2;
  --navy:#0b1a33;
  --ink:#1f2327;
  --muted:#8a8f94;
  --line:#d7e6f3;
  --grey-bg:#f4f4f4;
  --charcoal:#2e3138;
  --green:#4cb84c;
  --white:#fff;
}
*{box-sizing:border-box;margin:0;padding:0}
html,body{width:1200px;height:2899px;overflow:hidden;background:var(--white)}
body{font-family:"Open Sans",Arial,sans-serif;color:var(--ink);position:relative}
.btn{position:absolute;display:flex;align-items:center;justify-content:center;font-size:11px;font-weight:600;letter-spacing:.5px;text-transform:uppercase;color:var(--white);background:var(--blue)}

/* hero */
.hero{position:absolute;left:0;top:0;width:1200px;height:520px;background:radial-gradient(ellipse at 70% 35%,#1f5f8c 0%,#0f2f55 35%,var(--navy) 75%)}
.hero-art{position:absolute;left:560px;top:0;width:520px;height:520px;background:radial-gradient(circle at 40% 40%,rgba(90,200,230,.45),rgba(240,160,40,.18) 30%,rgba(11,26,51,0) 65%)}
.brand{position:absolute;left:77px;top:26px;color:var(--white);font-weight:700}
.brand-name{font-size:32px;letter-spacing:1px;line-height:1}
.brand-sub{font-size:11px;letter-spacing:.6px;margin-top:3px}
.nav{position:absolute;left:396px;top:44px;display:flex;gap:26px;font-size:11px;color:var(--white);text-transform:uppercase}
.nav .active{color:var(--blue);position:relative}
.nav .active::before{content:"";position:absolute;left:0;right:0;top:-44px;height:3px;background:var(--blue)}
.nav .call{font-weight:700;display:flex;align-items:center;gap:5px}
.hero h1{position:absolute;left:156px;top:218px;font-size:38px;font-weight:400;color:var(--white)}
.hero .tagline{position:absolute;left:156px;top:264px;font-size:24px;color:var(--white)}
.dots{position:absolute;display:flex;gap:6px}
.dots span{width:7px;height:7px;border-radius:50%;border:1px solid var(--blue)}
.dots span.on{background:var(--blue)}
.hero .dots span{border-color:#9fb4c8}
.hero .dots span.on{background:#c9d6e2}

/* welcome */
.welcome h2{position:absolute;left:0;width:1200px;top:578px;text-align:center;font-size:26px;font-weight:400}
.rule{position:absolute;left:530px;top:617px;width:140px;height:1px;background:#cfd3d6}
.welcome p{position:absolute;left:200px;width:800px;top:638px;text-align:center;font-size:11.5px;line-height:18px;color:var(--muted);white-space:nowrap}

/* offer */
.offer{position:absolute;left:0;top:844px;width:1200px;height:327px;background:var(--blue);color:var(--white)}
.offer h2{position:absolute;left:156px;top:96px;font-size:24px;font-weight:400}
.offer .lead{position:absolute;left:156px;top:134px;width:390px;font-size:12.5px;line-height:20px}
.offer .btn{left:156px;top:204px;width:136px;height:32px;background:var(--charcoal)}
.acc{position:absolute;left:612px;width:431px;border:1px solid rgba(255,255,255,.55);color:var(--white)}
.acc-head{height:37px;display:flex;align-items:center;justify-content:space-between;padding:0 22px;font-family:Oswald,sans-serif;font-size:14px;text-transform:uppercase;letter-spacing:.3px}
.acc-head i{width:12px;height:12px;border-radius:50%;background:rgba(255,255,255,.75);position:relative}
.acc-head i::after{content:"";position:absolute;left:3px;top:5.5px;width:6px;height:1px;background:var(--blue)}
.acc-head i.plus::before{content:"";position:absolute;left:5.5px;top:3px;width:1px;height:6px;background:var(--blue)}
.acc-body{border-top:1px solid rgba(255,255,255,.55);padding:13px 22px;font-size:11px;line-height:18px}

/* services */
.photo{position:absolute;width:358px;height:199px}
.photo-a{left:232px;top:1235px;background:linear-gradient(135deg,#e9eef2,#b9c6d1 55%,#6f7f8e)}
.photo-b{left:610px;top:1235px;background:linear-gradient(135deg,#8fa4b6,#4c5f72 55%,#2b3a48)}
.svc h3{position:absolute;top:1452px;font-family:Oswald,sans-serif;font-weight:400;font-size:15px;text-transform:uppercase}
.svc p{position:absolute;top:1481px;width:358px;font-size:11.5px;line-height:17px;color:var(--muted)}
.btn-ghost{background:var(--white);color:var(--blue);border:1px solid var(--blue)}

/* testimonials */
.voices{position:absolute;left:0;top:1660px;width:1200px;height:405px;background:var(--grey-bg)}
.voices h2{position:absolute;left:0;width:1200px;top:54px;text-align:center;font-size:25px;font-weight:400}
.avatar{position:absolute;width:51px;height:51px;border-radius:50%;background:linear-gradient(#c9b3a4,#8e7566)}
.quote{position:absolute;top:138px;width:350px;font-size:11.5px;line-height:21px;color:var(--muted);white-space:nowrap}
.who{position:absolute;top:264px;font-size:12px;font-weight:700}
.where{position:absolute;top:284px;font-size:10px;color:var(--muted);text-transform:uppercase}

/* cta */
.cta{position:absolute;left:0;top:2065px;width:1200px;height:120px;background:var(--charcoal);color:var(--white)}
.cta h2{position:absolute;left:156px;top:28px;font-size:24px;font-weight:400}
.cta p{position:absolute;left:156px;top:66px;font-size:13px}
.cta .btn{left:908px;top:44px;width:136px;height:32px;background:var(--green)}

/* contact */
.contact h2{position:absolute;left:156px;top:2280px;font-size:25px;font-weight:400;line-height:32px}
.contact p{position:absolute;left:156px;top:2356px;width:340px;font-size:12px;line-height:19px;color:var(--muted)}
.field{position:absolute;border:2px solid var(--line);font-size:11px;color:var(--muted);padding:8px 12px}
.send{position:absolute;left:1002px;top:2430px;width:32px;height:32px;border-radius:50%;background:var(--blue)}

/* map */
.map{position:absolute;left:0;top:2514px;width:1200px;height:319px;background:linear-gradient(90deg,#d9dadb,#ecedee 40%,#f1f1f1)}
.card{position:absolute;left:156px;top:2514px;width:279px;height:319px;background:var(--blue);color:var(--white);padding:56px 32px 0}
.card h4{font-size:13px;font-weight:600;text-transform:uppercase;margin-bottom:16px}
.card .addr{font-size:12px;line-height:19px;margin-bottom:14px}
.card .tel{font-size:15px;line-height:20px}
.card .mail{font-size:11px}
.social{position:absolute;left:32px;top:242px;display:flex;gap:10px}
.social span{width:32px;height:32px;border:1px solid rgba(255,255,255,.7)}
.social span.on{background:var(--white)}
.pin{position:absolute;left:820px;top:2664px}

/* footer */
.footer{position:absolute;left:0;top:2833px;width:1200px;height:66px;font-size:11px;color:var(--muted)}
.footer .copy{position:absolute;left:156px;top:27px}
.footer .links{position:absolute;right:156px;top:27px}
.footer .links .on{color:var(--blue)}
</style>
</head>
<body>

<header class="hero">
  <div class="hero-art" role="img" aria-label="Hand reaching toward a glowing cube of blue and orange blocks over a network backdrop"></div>
  <div class="brand"><div class="brand-name">BIRCHWELL</div><div class="brand-sub">VENTURE ADVISORS</div></div>
  <nav class="nav">
    <span class="active">Home</span><span>About Us</span><span>Services</span><span>Testimonial</span><span>Contact Us</span>
    <span class="call">Call:
      <svg width="10" height="10" viewBox="0 0 24 24"><path fill="#fff" d="M6.6 10.8a15 15 0 0 0 6.6 6.6l2.2-2.2c.3-.3.7-.4 1-.2 1.1.4 2.3.6 3.6.6.6 0 1 .4 1 1V20c0 .6-.4 1-1 1A17 17 0 0 1 3 4c0-.6.4-1 1-1h3.5c.6 0 1 .4 1 1 0 1.3.2 2.5.6 3.6.1.3 0 .7-.2 1z"/></svg>
      512-555-0147</span>
  </nav>
  <div class="btn" style="left:983px;top:35px;width:120px;height:35px;background:var(--green)">Consult Now!</div>
  <h1>We Uncover &amp; implement</h1>
  <div class="tagline">the right solution, at the right time, in the right way.</div>
  <div class="btn" style="left:156px;top:321px;width:136px;height:31px">Explore More</div>
  <div class="dots" style="left:574px;top:472px"><span></span><span class="on"></span><span></span><span></span></div>
</header>

<section class="welcome">
  <h2>Welcome to Birchwell Venture Advisors</h2>
  <div class="rule"></div>
  <p>We are consulting/manufacturer representative company in Lorem ipsum dolor sit amet, consectetur<br>adipiscing elit, sed do eiusmod tempor incididunt ut labore et dolore magna aliqua. Ut enim ad minim veniam, quis nostrud<br>exercitation ullamco laboris nisi ut aliquip ex ea commodo consequat. Duis aute irure dolor in<br>reprehenderit in voluptate velit esse cillum dolore eu fugiat nulla pariatur.</p>
  <div class="btn" style="left:531px;top:738px;width:136px;height:31px;border:1px solid var(--blue-dark)">More About Us</div>
</section>

<section class="offer">
  <h2>What We Offer?</h2>
  <p class="lead">Serving Energy, Public, Transportation &amp; Logistics and Business Services – cleaner, safer, more economical.</p>
  <div class="btn">Contact Us</div>
  <div class="acc" style="top:49px">
    <div class="acc-head">Corporate Performance Improvement<i></i></div>
    <div class="acc-body">Lorem ipsum dolor sit amet, consectetur adipiscing elit, sed do eiusmod tempor incididunt ut labore et dolore magna aliqua. Ut enim ad minim veniam, quis nostrud exercitation ... [+]</div>
  </div>
  <div class="acc" style="top:190px"><div class="acc-head">Strategy &amp; Value Creation<i class="plus"></i></div></div>
  <div class="acc" style="top:242px"><div class="acc-head">We Turn Stagnation Into Growth<i class="plus"></i></div></div>
</section>

<section class="svc">
  <div class="photo photo-a" role="img" aria-label="Consultant presenting charts on a whiteboard to a seated team"></div>
  <div class="photo photo-b" role="img" aria-label="Project team discussing work around a meeting table"></div>
  <h3 style="left:232px">Consulting &amp; Training Services</h3>
  <p style="left:232px">Nemo enim ipsam voluptatem quia voluptas sit aspernatur aut odit aut fugit, sed quia consequuntur magni dolores eos qui ratione voluptatem sequi nesciunt.</p>
  <div class="btn btn-ghost" style="left:232px;top:1563px;width:112px;height:33px">Learn More</div>
  <h3 style="left:610px">We Offer Project Management</h3>
  <p style="left:610px">Nemo enim ipsam voluptatem quia voluptas sit aspernatur aut odit aut fugit, sed quia consequuntur magni dolores eos qui ratione voluptatem sequi nesciunt.</p>
  <div class="btn" style="left:610px;top:1563px;width:112px;height:33px">Learn More</div>
</section>

<section class="voices">
  <h2>What Our People are Saying?</h2>
  <div class="avatar" style="left:156px;top:144px" role="img" aria-label="Client portrait"></div>
  <p class="quote" style="left:232px">" Lorem ipsum dolor sit amet, consectetur adipiscing<br>elit, sed do eiusmod tempor incididunt ut labore et dolore<br>magna aliqua. Ut enim ad minim veniam, quis nostrud<br>exercitation ullamco laboris nisi ut aliquip ex ea<br>commodo consequat ...</p>
  <div class="who" style="left:232px">- Marcus D.</div>
  <div class="where" style="left:232px">Chicago, Illinois</div>
  <div class="avatar" style="left:612px;top:144px" role="img" aria-label="Client portrait"></div>
  <p class="quote" style="left:688px">" Lorem ipsum dolor sit amet, consectetur adipiscing<br>elit, sed do eiusmod tempor incididunt ut labore et dolore<br>magna aliqua. Ut enim ad minim veniam, quis nostrud<br>exercitation ullamco laboris nisi ut aliquip ex ea<br>commodo consequat ...</p>
  <div class="who" style="left:688px">- Helen R.</div>
  <div class="where" style="left:688px">Arlington, Washington</div>
  <div class="dots" style="left:574px;top:335px"><span></span><span class="on"></span><span></span><span></span></div>
</section>

<section class="cta">
  <h2>Do you need help for Improve Your Business?</h2>
  <p>Get help from a expert and knowledgeable professional.</p>
  <div class="btn">Consult Now!</div>
</section>

<section class="contact">
  <h2>Don't know where to start?<br>Let's get in touch!</h2>
  <p>Let us know what we can do to make your life easier and feel confident that your loved one is getting the care they deserve.</p>
  <div class="field" style="left:610px;top:2251px;width:433px;height:32px">Your Name</div>
  <div class="field" style="left:610px;top:2295px;width:207px;height:32px">Email</div>
  <div class="field" style="left:838px;top:2295px;width:205px;height:32px">Phone</div>
  <div class="field" style="left:610px;top:2338px;width:433px;height:112px">Message ...</div>
  <div class="send"><svg width="32" height="32" viewBox="0 0 32 32"><path fill="#fff" d="M10 10l13 6-13 6 2-6z"/></svg></div>
</section>

<div class="map" role="img" aria-label="Grey road map of Texas and New Mexico"></div>
<svg class="pin" width="18" height="26" viewBox="0 0 18 26"><path fill="#1f2327" d="M9 0a9 9 0 0 0-9 9c0 7 9 17 9 17s9-10 9-17a9 9 0 0 0-9-9zm0 12.5A3.5 3.5 0 1 1 9 5.5a3.5 3.5 0 0 1 0 7z"/></svg>
<div class="card">
  <h4>Contact Us</h4>
  <div class="addr">1180 Cedar Hollow Rd<br>Austin, Texas - 78701</div>
  <div class="tel">P. 512-555-0147</div>
  <div class="mail">E. info@birchwell.com</div>
  <div class="social"><span></span><span class="on"></span><span></span><span></span></div>
</div>

<footer class="footer">
  <div class="copy">Copyright ©2018 Birchwell Venture Advisors. All rights reserved.</div>
  <div class="links"><span class="on">Home</span> &nbsp;|&nbsp; About &nbsp;|&nbsp; Contact Us</div>
</footer>

</body>
</html>
```